Carrow Tessel Hair Extensions needs a packaging design

We need a packaging design for a new hair extension company based in Edmonton, Alberta called Lusine Oro. Our packaging should communicate high quality, luxurious hair that will never tangle or dry out. The product will be marketed to salon professionals as well as clients. We would like to see designs that include but not restricted to the colours gold black and white.

Reason: Although we were very impressed with the designs that came though thus far, we are hoping to receive a few more ideas before making a final decision. Thank you!

Target Market(s)

Women and beauty industry professionals. High end market.

Industry/Entity Type

Hair

Requirements
Must have
• "Highest quality 100% Remi hair!" should be written on the front of the package. In addition, we would like to add text to the back of the packaging as follows:
• Hair Collection and Color Processing:
• Only the highest quality hair is selected which ensures high moisture and nutrient content
• The hair is directly cut from the donor which ensures that the hair cuticle remains intact and always tangle-free
• No chemicals are used in dyeing the hair
• The hair will never fade due to the mild and healthy herbal extract used in the dyeing process which gently penetrates to the inner core of the hair
• Care Instructions:
• Lusine Oro provides only the highest in quality Remi hair that demands very little care to maintain it’s luxurious feel.
• Use a proper extension bristle brush
• Wash the hair with a sulfate-free shampoo and follow with a moisturizing conditioner that is formulated for hair extensions
• Do not apply any type of chemicals to the hair
• We proudly show our immense passion for delivering superior quality in our full product line.
• We insist that it is important for you to know and understand what you are purchasing in your hair extensions. We guarantee the highest quality of our products.
• Lusine Oro is strongly committed to serving their clients with utmost integrity, believing in a foundation of personal and professional ethics and our 20 years service in the beauty industry.
Nice to have
• I would like the background to be white with the "M" in gold. My concern is that this may look too plain, but with that said, I don't want the design to be too busy. Keeping it classy is my main goal.

```html
<!DOCTYPE html>
<html lang="en">
<head>
<meta charset="utf-8">
<title>Lusine Oro — Packaging</title>
<link rel="stylesheet" href="https://fonts.googleapis.com/css2?family=Arimo:wght@400;700&family=Great+Vibes&display=swap">
<style>
  :root {
    --canvas: #ffffff;
    --frame: #dcdcdc;
    --ink: #111111;
    --orange-deep: #ff8a00;
    --orange: #ffae00;
    --orange-light: #ffc21a;
    --gold: #c9962b;
    --gold-light: #f2d36b;
    --yellow: #ffef00;
    --pink: #d43a6a;
    --red-script: #e8254f;
    --silver: #9a9a9a;
    --box-top: #ffffff;
    --box-bottom: #e2e2e2;
  }
  html, body {
    margin: 0;
    padding: 0;
    width: 1001px;
    height: 1200px;
    overflow: hidden;
    background: var(--canvas);
  }
  .packaging {
    display: block;
    width: 1001px;
    height: 1200px;
  }
  .brand-name {
    font-family: "Arimo", Arial, sans-serif;
    font-weight: 400;
  }
  .script-line {
    font-family: "Great Vibes", cursive;
  }
  .feature-line {
    font-family: "Arimo", Arial, sans-serif;
    font-size: 12px;
    fill: var(--ink);
  }
  .ribbon-text {
    font-family: "Arimo", Arial, sans-serif;
    font-weight: 400;
    fill: var(--yellow);
  }
</style>
</head>
<body>
<svg class="packaging" viewBox="0 0 1001 1200" xmlns="http://www.w3.org/2000/svg">
  <defs>
    <linearGradient id="boxBody" x1="0" y1="0" x2="0" y2="1">
      <stop offset="0.35" stop-color="var(--box-top)"/>
      <stop offset="0.7" stop-color="var(--box-bottom)"/>
    </linearGradient>
    <radialGradient id="orangePanel" cx="0.55" cy="0.3" r="0.8">
      <stop offset="0" stop-color="var(--orange-light)"/>
      <stop offset="0.6" stop-color="var(--orange)"/>
      <stop offset="1" stop-color="var(--orange-deep)"/>
    </radialGradient>
    <linearGradient id="goldSweep" x1="0" y1="1" x2="1" y2="0">
      <stop offset="0" stop-color="var(--gold)"/>
      <stop offset="0.45" stop-color="#8c8c8c"/>
      <stop offset="0.7" stop-color="var(--yellow)"/>
      <stop offset="1" stop-color="var(--gold)"/>
    </linearGradient>
    <linearGradient id="headerStrip" x1="0" y1="0" x2="1" y2="0">
      <stop offset="0" stop-color="var(--pink)"/>
      <stop offset="0.5" stop-color="var(--yellow)"/>
      <stop offset="1" stop-color="var(--gold)"/>
    </linearGradient>
    <linearGradient id="ovalRing" x1="0" y1="0" x2="1" y2="1">
      <stop offset="0" stop-color="var(--gold)"/>
      <stop offset="0.5" stop-color="var(--gold-light)"/>
      <stop offset="1" stop-color="var(--gold)"/>
    </linearGradient>
    <radialGradient id="ovalFill" cx="0.5" cy="0.5" r="0.6">
      <stop offset="0.5" stop-color="#ffffff"/>
      <stop offset="1" stop-color="#dedede"/>
    </radialGradient>
  </defs>

  <!-- canvas frame -->
  <rect class="canvas-frame" x="2" y="2" width="997" height="1196" fill="none" stroke="var(--frame)" stroke-width="3"/>

  <!-- box: header cap -->
  <g class="box-header">
    <rect x="207" y="38" width="332" height="63" fill="var(--ink)"/>
    <rect x="207" y="101" width="332" height="6" fill="url(#headerStrip)"/>
    <text class="brand-name" x="373" y="79" font-size="24" fill="var(--gold-light)" text-anchor="middle">Lusine Oro</text>
  </g>

  <!-- box: body -->
  <g class="box-front">
    <rect x="204" y="118" width="338" height="1047" fill="url(#boxBody)"/>
    <rect x="204" y="118" width="3" height="1047" fill="#d4d4d4"/>
    <path class="gold-swoosh" d="M541,322 C522,405 440,428 360,446 C280,464 220,486 206,525 L206,620 C222,548 282,506 362,486 C452,464 530,432 541,348 Z" fill="url(#goldSweep)"/>
    <path class="orange-panel" d="M207,118 H541 V318 C522,398 440,420 360,438 C280,456 220,478 206,515 Z" fill="url(#orangePanel)"/>
    <path class="black-edge" d="M541,322 C522,402 440,424 360,442 C280,460 220,482 206,520" fill="none" stroke="var(--ink)" stroke-width="9"/>

    <g class="new-ribbon">
      <polygon points="433,119 477,119 541,158 541,196" fill="var(--pink)"/>
      <text class="ribbon-text" x="500" y="158" font-size="26" text-anchor="middle" transform="rotate(32 500 150)">NEW</text>
    </g>

    <g class="name-oval">
      <ellipse cx="373" cy="231" rx="104" ry="64" fill="url(#ovalFill)" stroke="url(#ovalRing)" stroke-width="8"/>
      <text class="brand-name" x="373" y="242" font-size="32" fill="var(--ink)" text-anchor="middle">Lusine Oro</text>
    </g>

    <text class="script-line" x="371" y="340" font-size="32" fill="#2a2a2a" text-anchor="middle">Premium Hair Extension</text>
    <text class="feature-line" x="380" y="361" text-anchor="middle">HIGH QUALITY ■ LUXURIOUS ■ NO TANGLES</text>
  </g>

  <!-- hang tag string -->
  <path class="tag-string" d="M664,842 C652,828 656,808 654,792 L626,408 C622,338 774,338 772,408 L736,770 C734,800 746,818 718,832" fill="none" stroke="var(--silver)" stroke-width="5" stroke-linecap="round"/>

  <!-- hang tag -->
  <g class="hang-tag">
    <path class="tag-gold" d="M510,835 L718,826 Q800,834 800,962 L800,1160 L640,1164 Q514,1150 510,1040 Z" fill="url(#goldSweep)"/>
    <path class="tag-orange" d="M510,838 L690,832 Q780,840 790,980 L790,1152 L652,1150 Q522,1138 510,1052 Z" fill="url(#orangePanel)"/>
    <path class="tag-black-top" d="M690,832 Q780,840 790,980" fill="none" stroke="var(--ink)" stroke-width="5"/>
    <path class="tag-black-bottom" d="M652,1150 Q522,1138 510,1052" fill="none" stroke="var(--ink)" stroke-width="5"/>
    <circle class="tag-hole" cx="668" cy="847" r="6" fill="#ffffff" stroke="#cccccc" stroke-width="1"/>

    <g class="new-ribbon">
      <polygon points="510,860 548,832 590,830 510,890" fill="var(--pink)"/>
      <text class="ribbon-text" x="541" y="866" font-size="19" text-anchor="middle" transform="rotate(-35 541 860)">NEW</text>
    </g>

    <text class="brand-name" x="657" y="1005" font-size="34" fill="var(--ink)" text-anchor="middle">Lusine Oro</text>
    <text class="script-line" x="660" y="1038" font-size="25" fill="var(--red-script)" text-anchor="middle">Premium Hair Extension</text>
    <text class="feature-line" x="660" y="1055" font-size="10.5" text-anchor="middle" style="font-size:10.5px">HIGH QUALITY ■ LUXURIOUS ■ NO TANGLES</text>
  </g>
</svg>
</body>
</html>
```